" Nosso corpo jurídico é constituído por profissionais com vasta experiência na advocacia. A reunião desses profissionais e o amadurecimento de um ideal comum, resultaram na criação de um grupo comprometido com a prestação de serviços jurídicos. Estamos aptos a atender, com eficiência, agilidade e qualidade, atuando em equipe ou individualmente para solução do seu problema, por meio de métodos eficientes e dinâmicos. "

```html
<!DOCTYPE html>
<html lang="pt-BR">
<head>
<meta charset="utf-8">
<title>Moreira Tavares &amp; Lins — Cartão de Visita</title>
<link rel="stylesheet" href="https://fonts.googleapis.com/css2?family=Cormorant+Garamond:wght@500;600&family=Montserrat:wght@400;500;600&display=swap">
<style>
  :root {
    --canvas: #e9e9e8;
    --card-dark: #3b312d;
    --card-light: #ffffff;
    --gold: #b88a5a;
    --ink: #4a4644;
    --ink-soft: #7a7674;
    --rule: #e4e0dc;
    --on-dark: #f4efe9;
  }
  * { box-sizing: border-box; margin: 0; padding: 0; }
  html, body {
    width: 1200px; height: 1200px; overflow: hidden;
    background: var(--canvas);
  }
  .sheet {
    width: 1200px; height: 1200px;
    display: flex; flex-direction: column; align-items: center; justify-content: center;
    gap: 60px;
  }
  .card {
    width: 900px; height: 514px;
    box-shadow: 0 6px 18px rgba(0,0,0,.12);
    position: relative;
  }

  /* Front */
  .card--front {
    background: var(--card-dark);
    display: flex; flex-direction: column; align-items: center; justify-content: center;
    gap: 34px;
  }
  .brand-mark {
    width: 64px; height: 64px; border: 5px solid var(--gold);
  }
  .brand-name--front {
    font-family: "Montserrat", sans-serif;
    font-weight: 500; font-size: 30px; letter-spacing: .32em;
    color: var(--on-dark); text-transform: uppercase;
  }

  /* Back */
  .card--back {
    background: var(--card-light);
    padding: 64px 70px;
    font-family: "Montserrat", sans-serif;
    color: var(--ink);
  }
  .brand-row { display: flex; align-items: center; gap: 22px; }
  .brand-row .brand-mark { width: 48px; height: 48px; border-width: 4px; }
  .brand-name--back {
    font-family: "Cormorant Garamond", serif;
    font-weight: 600; font-size: 40px; line-height: 1.05;
    text-transform: uppercase; color: var(--ink); letter-spacing: .02em;
  }
  .details {
    display: grid; grid-template-columns: 1fr 1fr; gap: 0 40px;
    margin-top: 58px;
  }
  .details__col { display: flex; flex-direction: column; gap: 14px; }
  .details__col--right { padding-top: 50px; border-left: 1px solid var(--rule); padding-left: 60px; }
  .line { display: flex; align-items: center; gap: 12px; font-size: 21px; color: var(--ink); }
  .line svg { width: 22px; height: 22px; flex: none; fill: var(--gold); }
  .person__name { color: var(--gold); font-weight: 600; letter-spacing: .04em; font-size: 22px; }
  .person__role { font-size: 14px; letter-spacing: .12em; color: var(--ink-soft); margin: -10px 0 4px 34px; }
</style>
</head>
<body>
<main class="sheet">
  <section class="card card--front" aria-label="Frente do cartão">
    <div class="brand-mark"></div>
    <p class="brand-name--front">Moreira Tavares &amp; Lins</p>
  </section>

  <section class="card card--back" aria-label="Verso do cartão">
    <div class="brand-row">
      <div class="brand-mark"></div>
      <p class="brand-name--back">Moreira Tavares<br>&amp; Lins</p>
    </div>

    <div class="details">
      <div class="details__col">
        <p class="line person__name">
          <svg viewBox="0 0 24 24"><rect x="2" y="2" width="20" height="20" rx="3"/><circle cx="12" cy="10" r="4" fill="#fff"/><path d="M5 20c1-4 4-5 7-5s6 1 7 5z" fill="#fff"/></svg>
          NOME SOBRENOME
        </p>
        <p class="person__role">CARGO/FUNÇÃO</p>
        <p class="line">
          <svg viewBox="0 0 24 24"><path d="M6.6 10.8a15 15 0 0 0 6.6 6.6l2.2-2.2a1 1 0 0 1 1-.25 11.4 11.4 0 0 0 3.6.57 1 1 0 0 1 1 1V20a1 1 0 0 1-1 1A17 17 0 0 1 3 4a1 1 0 0 1 1-1h3.5a1 1 0 0 1 1 1c0 1.25.2 2.45.57 3.57a1 1 0 0 1-.25 1z"/></svg>
          99 99999-9999
        </p>
        <p class="line">
          <svg viewBox="0 0 24 24"><path d="M2 5h20v14H2z"/><path d="M2 5l10 8 10-8" fill="none" stroke="#fff" stroke-width="2"/></svg>
          nome@empresa.com.br
        </p>
      </div>
      <div class="details__col details__col--right">
        <p class="line">
          <svg viewBox="0 0 24 24"><circle cx="12" cy="12" r="10"/><path d="M2 12h20M12 2c3 3 3 17 0 20M12 2c-3 3-3 17 0 20" fill="none" stroke="#fff" stroke-width="1.5"/></svg>
          www.site.com.br
        </p>
        <p class="line">
          <svg viewBox="0 0 24 24"><rect x="6" y="2" width="12" height="20" rx="2"/><rect x="8" y="5" width="8" height="12" fill="#fff"/></svg>
          99 9999-9999
        </p>
        <p class="line">
          <svg viewBox="0 0 24 24"><path d="M12 2a7 7 0 0 0-7 7c0 5 7 13 7 13s7-8 7-13a7 7 0 0 0-7-7z"/><circle cx="12" cy="9" r="2.5" fill="#fff"/></svg>
          Rua do Projeto, 999
        </p>
      </div>
    </div>
  </section>
</main>
</body>
</html>
```